Bakery Business Cards

We are in need of business cards for our bakery business--something non-generic that reflects our business and will stand out. We are a wholesale bakery that primarily services in-store bakeries, casinos, schools, distributors, and fund-raising companies. The family business was founded in 1960. (www.marlowsovenworks.com)

```html
<!DOCTYPE html>
<html lang="en">
<head>
<meta charset="utf-8">
<title>Marlow's Ovenworks – Business Cards</title>
<link rel="stylesheet" href="https://fonts.googleapis.com/css2?family=Montserrat:wght@500;600&display=swap">
<style>
  :root {
    --backdrop: #d9d9d7;
    --crust-red: #8f1a1d;
    --crust-red-soft: #a0392c;
    --dough: #efb75d;
    --dough-deep: #e3a24f;
    --cream: #ffffff;
  }
  html, body {
    margin: 0;
    padding: 0;
    width: 1200px;
    height: 900px;
    overflow: hidden;
    background: var(--backdrop);
    font-family: "Montserrat", sans-serif;
  }
  .canvas {
    position: relative;
    width: 1200px;
    height: 900px;
  }
  .card {
    position: absolute;
    width: 560px;
    height: 320px;
    background: var(--crust-red);
    box-shadow: 0 3px 8px rgba(0,0,0,0.25);
    overflow: hidden;
  }
  .card--contact { left: 70px; top: 90px; }
  .card--brand { left: 570px; top: 490px; }

  .watermark-area {
    position: absolute;
    left: 110px;
    top: 20px;
    width: 380px;
    height: 270px;
    border-radius: 50%;
    background: radial-gradient(ellipse at center, rgba(160,57,44,0.45), rgba(160,57,44,0) 70%);
  }
  .contact-details {
    position: absolute;
    left: 70px;
    top: 100px;
    color: var(--cream);
    text-transform: uppercase;
  }
  .contact-name { font-size: 17px; font-weight: 500; letter-spacing: 0.5px; margin: 0 0 12px; }
  .contact-phone { font-size: 15px; font-weight: 500; margin: 0 0 10px 40px; letter-spacing: 0.5px; }
  .contact-location { font-size: 13px; font-weight: 500; margin: 0 0 0 42px; }
  .contact-web {
    position: absolute;
    left: 0;
    right: 0;
    bottom: 34px;
    text-align: center;
    color: var(--cream);
    font-size: 14px;
    font-weight: 500;
  }
  .wordmark {
    position: absolute;
    font-weight: 600;
    line-height: 1.05;
    margin: 0;
  }
  .card--contact .wordmark {
    right: 34px;
    top: 200px;
    color: var(--cream);
    font-size: 20px;
    text-align: center;
  }
  .dough-panel { position: absolute; inset: 0; }
  .card--brand .wordmark {
    left: 0;
    right: 0;
    top: 120px;
    text-align: center;
    color: var(--crust-red);
    font-size: 34px;
  }
</style>
</head>
<body>
<main class="canvas">
  <section class="card card--contact">
    <div class="watermark-area" role="img" aria-label="Faint brand symbol decoration"></div>
    <div class="contact-details">
      <p class="contact-name">Name</p>
      <p class="contact-phone">9XXXXXXXX8</p>
      <p class="contact-location">Location</p>
    </div>
    <p class="wordmark">Marlow's<br>Ovenworks</p>
    <p class="contact-web">www.marlowsovenworks.com</p>
  </section>

  <section class="card card--brand">
    <svg class="dough-panel" width="560" height="320" viewBox="0 0 560 320" aria-hidden="true">
      <path fill="var(--dough)" d="M40 32 C90 18 130 40 190 30 C260 18 320 38 390 28 C450 20 500 36 528 40 C540 80 520 120 534 170 C546 220 520 250 530 292 C480 302 430 284 370 296 C300 308 240 288 170 298 C110 306 70 290 30 294 C24 250 40 210 28 160 C18 110 40 80 40 32 Z"/>
    </svg>
    <div class="watermark-area" role="img" aria-label="Faint brand symbol decoration" style="background: radial-gradient(ellipse at center, rgba(227,162,79,0.8), rgba(227,162,79,0) 70%); left: 90px; top: 25px;"></div>
    <p class="wordmark">Marlow's<br>Ovenworks</p>
  </section>
</main>
</body>
</html>
```